Easy Business Card / Presentation Cover Design Project

We are looking for a business card design, covers for powerpoint presentations for investors, and possibly simple stationary for a Chicago real estate development firm. Our new logo is attached below.

We rehab and provide newly constructed homes. We are not a real estate brokerage firm (i.e., agents such as Meridale 47) and only operate in the Chicago area.

In terms of design, sophisticated and high end that would appeal to investors (theme should resemble investment banks, hedge funds, private equity rather than tech startup).

Target Market(s)

Investors, banks, financing sources

Industry/Entity Type

Real Estate

Requirements
Must have
• Two deliverables here. 1) Business card 2) Covers for powerpoint presentation.

Must be able to look sophisticated and high end when printed. Please think through the type of printing that will be needed. Would prefer something that can be printed in raised ink but digital is ok as well.

Will be printed on heavy paper.

Business Card: Horizontal Layout, no black backgrounds,

For presentation front cover, should include logo only. For back cover, should include contact info. Horizontal and should not contain any information that will need to be changed (i.e. date or client name)
Nice to have
• Would like to have the edges colored but not required. Please show multiple designs
Should not have
• Should not have any die cut or embossed type of designs. Shape should be standard size.

We are not a design firm, a retail firm, or a consumer product firm.

Please do not incorporate a house, buildings, etc. This must be very professional looking.

```html
<!DOCTYPE html>
<html lang="en">
<head>
<meta charset="utf-8">
<title>Harlow Crest Business Card</title>
<link rel="stylesheet" href="https://fonts.googleapis.com/css2?family=Open+Sans:wght@400;600&display=swap">
<style>
  :root {
    --page-bg: #eceef2;
    --card-white: #ffffff;
    --blue-deep: #3467b2;
    --blue-soft: #8eaad9;
    --blue-pale: #a9bfe4;
    --grey-text: #7a7a7a;
    --grey-dark: #555558;
    --grey-light: #bcbcbe;
    --icon-dark: #4a4a4c;
    --shadow: 0 10px 28px rgba(40, 50, 70, 0.18);
  }
  * { margin: 0; padding: 0; box-sizing: border-box; }
  html, body { width: 1200px; height: 900px; overflow: hidden; }
  body {
    background: var(--page-bg);
    font-family: "Open Sans", Arial, sans-serif;
    position: relative;
  }
  .card {
    position: absolute;
    left: 250px;
    width: 700px;
    height: 400px;
    box-shadow: var(--shadow);
    overflow: hidden;
  }
  /* Back side */
  .card-back {
    top: 35px;
    background: linear-gradient(90deg,
      var(--blue-soft) 0%, var(--blue-soft) 22%,
      var(--blue-deep) 28%, var(--blue-deep) 72%,
      var(--blue-soft) 78%, var(--blue-pale) 100%);
  }
  .back-brand {
    position: absolute;
    top: 50%; left: 50%;
    transform: translate(-50%, -50%);
    display: flex;
    align-items: center;
    gap: 16px;
  }
  .brand-dot {
    width: 64px; height: 64px;
    border-radius: 50%;
    border: 3px solid currentColor;
  }
  .brand-name {
    font-weight: 600;
    font-size: 38px;
    letter-spacing: 2px;
    line-height: 1;
  }
  .back-brand { color: #ffffff; }

  /* Front side */
  .card-front {
    top: 465px;
    background: var(--card-white);
  }
  .front-brand {
    position: absolute;
    top: 48px; left: 48px;
    display: flex;
    align-items: center;
    gap: 14px;
    color: var(--grey-text);
  }
  .front-brand .brand-dot { width: 54px; height: 54px; }
  .front-brand .brand-name { font-size: 32px; }

  .person {
    position: absolute;
    left: 80px; top: 220px;
    color: var(--grey-text);
  }
  .person-name {
    font-size: 42px;
    font-weight: 400;
    line-height: 1.1;
  }
  .person-title {
    font-size: 16px;
    font-weight: 600;
    margin-left: 30px;
    color: #6a6a6a;
  }
  .contact-list {
    position: absolute;
    left: 390px; top: 150px;
    list-style: none;
  }
  .contact-item {
    display: flex;
    align-items: center;
    gap: 12px;
    font-size: 17px;
    color: var(--grey-dark);
    margin-bottom: 12px;
  }
  .contact-icon {
    width: 26px; height: 26px;
    border-radius: 50%;
    background: var(--icon-dark);
    color: #fff;
    font-size: 13px;
    font-weight: 600;
    display: flex;
    align-items: center;
    justify-content: center;
    padding-bottom: 2px;
  }
  .front-bands {
    position: absolute;
    left: 0; bottom: 0;
    width: 700px; height: 70px;
  }
</style>
</head>
<body>
  <section class="card card-back" aria-label="Business card back">
    <div class="back-brand">
      <span class="brand-dot"></span>
      <span class="brand-name">HARLOW CREST</span>
    </div>
  </section>

  <section class="card card-front" aria-label="Business card front">
    <div class="front-brand">
      <span class="brand-dot"></span>
      <span class="brand-name">HARLOW CREST</span>
    </div>

    <div class="person">
      <p class="person-name">Evan Marsh</p>
      <p class="person-title">Branch Manager</p>
    </div>

    <ul class="contact-list">
      <li class="contact-item"><span class="contact-icon">p</span>312 555 0148</li>
      <li class="contact-item"><span class="contact-icon">e</span>evan@harlowcrest.com</li>
      <li class="contact-item"><span class="contact-icon">w</span>www.harlowcrest.com</li>
    </ul>

    <svg class="front-bands" viewBox="0 0 700 70" aria-hidden="true">
      <polygon points="0,50 700,22 700,70 0,70" fill="var(--grey-light)"/>
      <polygon points="110,46 505,30 518,44 110,70" fill="var(--grey-dark)"/>
      <polygon points="110,70 518,44 530,70" fill="var(--grey-dark)"/>
      <polygon points="512,29 555,27 570,42 528,44" fill="var(--blue-deep)"/>
      <polygon points="555,27 700,21 700,36 570,42" fill="var(--blue-soft)"/>
      <polygon points="0,70 110,70 110,58 0,62" fill="var(--grey-light)"/>
    </svg>
  </section>
</body>
</html>
```